Retail Jewelry Business Card Design Project

We are in need of a new business card design for a retail jewelry store. This store is in the business of fine jewelry including but not specific to bridal jewelry, diamonds, designer jewelry and watches.

This store has been in business for 20 years but continues to strive for a modern professional appeal. The main colors use for this business are a royal blue, white and silver.

Target Market(s)

Target market is ages 18-50

Industry/Entity Type

Jewelry

Requirements
Must have
• Sales Person Name
Sales Person Email Address

Store Address
Store Phone
Website

Standard business card size. No odd shapes or sizes.
Nice to have
• Overall modern feel for card.

We have thought that a design with a nice feature of the logo on the back of the card would be nice but open to ideas.
Should not have
• No specific images of jewelry should be used.

```html
<!DOCTYPE html>
<html lang="en">
<head>
<meta charset="utf-8">
<title>Marlow Grant Fine Jewelry – Business Card</title>
<link rel="stylesheet" href="https://fonts.googleapis.com/css2?family=EB+Garamond:wght@400;500&display=swap">
<style>
  :root {
    --backdrop: #e9e6e1;
    --card-black: #121212;
    --card-black-soft: #1c1c1c;
    --silver-light: #f2f2f2;
    --silver-mid: #c9c9c9;
    --silver-dark: #9a9a9a;
    --ink-dark: #3a3a3a;
    --ink-silver: #d6d6d6;
    --foil: #8f8f8f;
    --royal-blue: #2747b8;
  }
  * { box-sizing: border-box; margin: 0; padding: 0; }
  html, body { width: 1200px; height: 886px; overflow: hidden; }
  body {
    background: var(--backdrop);
    font-family: "EB Garamond", Georgia, serif;
    position: relative;
  }
  .card {
    position: absolute;
    top: 288px;
    width: 530px;
    height: 310px;
    border-radius: 6px;
    background: var(--card-black);
    overflow: hidden;
    box-shadow: 0 10px 24px rgba(0,0,0,0.25);
  }
  .card--front { left: 45px; }
  .card--back  { left: 625px; background: linear-gradient(180deg, var(--card-black-soft), var(--card-black)); }

  .front__brand {
    position: absolute;
    top: 20px; right: 40px;
    font-size: 24px;
    font-weight: 500;
    color: var(--ink-silver);
    letter-spacing: 0.5px;
    padding-bottom: 6px;
    border-bottom: 2px solid var(--royal-blue);
  }
  .front__band {
    position: absolute;
    left: 0; right: 0;
    top: 84px; height: 196px;
    background: linear-gradient(100deg, var(--silver-light) 0%, var(--silver-mid) 55%, var(--silver-dark) 100%);
    border-top: 3px solid var(--royal-blue);
  }
  .front__contact {
    position: absolute;
    right: 40px; top: 16px;
    text-align: right;
    color: var(--ink-dark);
    font-style: normal;
  }
  .contact__name { font-size: 19px; font-weight: 500; line-height: 1.2; }
  .contact__email { font-size: 14px; line-height: 1.3; }
  .contact__address { margin-top: 26px; font-size: 15px; line-height: 1.3; }
  .contact__phone { font-size: 15px; line-height: 1.3; color: var(--royal-blue); }

  .back__content {
    position: absolute;
    inset: 0;
    display: flex;
    flex-direction: column;
    align-items: center;
    justify-content: center;
    gap: 14px;
  }
  .back__brand {
    font-size: 36px;
    font-weight: 500;
    color: var(--foil);
    padding-bottom: 6px;
    border-bottom: 2px solid var(--royal-blue);
  }
  .back__web {
    font-size: 19px;
    color: var(--foil);
    letter-spacing: 0.5px;
  }
</style>
</head>
<body>
  <section class="card card--front">
    <div class="front__brand">Marlow Grant Fine Jewelry</div>
    <div class="front__band">
      <address class="front__contact">
        <p class="contact__name">Marlow Grant Hadley</p>
        <p class="contact__email">marlow@marlowgrantjewelry.com</p>
        <p class="contact__address">Marlow Grant Fine Jewelry<br>2280 Linden Avenue<br>Harbor Bay, FL 32900</p>
        <p class="contact__phone">(850) 555-0142</p>
      </address>
    </div>
  </section>

  <section class="card card--back">
    <div class="back__content">
      <p class="back__brand">Marlow Grant Fine Jewelry</p>
      <p class="back__web">www.marlowgrantjewelry.com</p>
    </div>
  </section>
</body>
</html>
```